Website Design for Non-profit

We are looking for a new site design for the Patrons of the Northern Heritage Hall. The current site can be found at
http://www.patrons-hall.org/pnhhindex_e.html
The URL is provided for reference. We want a completely different look and layout which is shown in the specifications document. Visiting the site, you can learn more about the organization.
Initially, we would like a home page, and inside page provided. Once we a home page and inside page are selected, we would like a simple mobile template provided.
I have attached a full description of the project as well as the specifications document and a zip file containing images for the site.
As mentioned in the specs document, we want to include an image of the museum in the header. The zip file is too large for us to upload (80 meg). The zip file can be obtained by clicking this link:
http://qzl.cc/TrWpKe
The zip file contains several exterior photos and you can select the one you feel is most appropriate to your design.
Reason: A long weekend is coming up and a few members of the team are unavailable for review.
Reason: Reviewing designs. Should have a decision next week.
Reason: We are discussing the designs and looking to reach a consensus. I will be implementing some designs today or tomorrow. Hopefully final selection will be next week.
Reason: Still reviewing designs. Hope to get a decision soon.
Reason: Working to finalize the design. Very close.
Industry/Entity Type
Museum
Look and feel
Each slider illustrates characteristics of the customer's brand and the style your logo design should communicate.

```html
<!DOCTYPE html>
<html lang="en">
<head>
<meta charset="utf-8">
<title>Patrons of the Northern Heritage Hall</title>
<link rel="stylesheet" href="https://fonts.googleapis.com/css2?family=Ubuntu:wght@400;500&family=Noto+Sans:wght@400;700&family=Arimo:wght@400;700&display=swap">
<style>
:root{
  --bar:#2b2b2b; --nav:#3d3d3d; --gold:#9a8628; --gold-dark:#7d6c1d;
  --blue:#1ea3c8; --blue-dark:#1588ab; --ink:#222; --muted:#555;
  --panel:#f4f4f4; --line:#d6d6d6; --footer:#262626;
}
*{margin:0;padding:0;box-sizing:border-box}
html,body{width:1001px;height:1200px;overflow:hidden;background:#e9e9e9}
body{font-family:"Noto Sans",sans-serif;color:var(--ink)}
.page{position:relative;width:1001px;height:1200px;background:linear-gradient(#e2e2e2 503px,#f3f3f3 620px,#fafafa 1093px)}
.abs{position:absolute}
.topbar{left:0;top:0;width:1001px;height:33px;background:var(--bar);font-family:Arimo,sans-serif;font-size:11.5px;color:#fff}
.topbar a{position:absolute;top:10px;color:#fff;text-decoration:none}
.topbar .pill{top:7px;left:823px;width:88px;height:20px;border-radius:6px;background:var(--blue);text-align:center;line-height:20px;font-size:11px}
.topbar .media{top:8px;font-weight:700;font-size:11px}
.topbar .share{top:7px;left:289px;width:54px;height:19px;background:#3b5a98;border-radius:2px;font-size:8px;line-height:19px;text-align:center}
.header{left:0;top:33px;width:1001px;height:119px;background:linear-gradient(#fff,#ececec)}
.brand{left:88px;top:62px;display:flex;align-items:center;gap:10px;font-family:Ubuntu,sans-serif;font-weight:500;font-size:30px;color:var(--gold);letter-spacing:3px}
.brand i{display:block;width:26px;height:26px;background:var(--blue)}
.fontsize{left:560px;top:60px;font-size:10.5px;display:flex;align-items:center;gap:6px}
.fontsize span.c{display:inline-flex;align-items:center;justify-content:center;border-radius:50%;border:2px solid #7bbcd0;background:#f4f8fa;font-family:Arimo,sans-serif}
.connect{left:711px;top:58px;font-family:Ubuntu,sans-serif;font-size:14px;color:#888;display:flex;align-items:center;gap:5px}
.connect b{display:inline-block;width:20px;height:20px;border-radius:50%;background:#8b8b8b}
.connect b.sq{border-radius:2px}
.search{left:705px;top:95px;width:185px;height:32px;border-radius:16px;background:linear-gradient(#e4e4e4,#f8f8f8);border:1px solid #d9d9d9}
.hero{left:0;top:152px;width:1001px;height:313px;background:var(--gold)}
.hero .frame{position:absolute;left:87px;top:0;width:829px;height:292px;background:#fff}
.hero .photo{position:absolute;left:7px;top:5px;width:814px;height:277px;background:linear-gradient(#4f6fa0 0%,#f2c775 40%,#5a5548 58%,#7ea4d3 62%,#c3d7ee 100%)}
.nav{left:0;top:465px;width:1001px;height:38px;background:var(--nav);font-size:11px;color:#fff;letter-spacing:.4px}
.nav span{position:absolute;top:13px}
.nav .home{top:8px;left:96px;width:50px;height:23px;border-radius:3px;background:var(--blue);text-align:center;line-height:23px}
.nav i{position:absolute;top:0;width:1px;height:38px;background:#222}
.tab{top:541px;height:37px;border-radius:6px 6px 0 0;font-family:Ubuntu,sans-serif;font-weight:500;font-size:14.5px;text-align:center;line-height:37px;color:#fff;background:var(--blue)}
.tab.active{background:#fff;color:var(--ink);border:1px solid var(--line);border-bottom:none;z-index:2}
.intro{left:83px;top:577px;width:833px;height:189px;background:linear-gradient(#fff,#ededed);border:1px solid var(--line)}
.intro p{position:absolute;left:18px;width:608px;font-size:10.5px;line-height:20px;text-align:justify}
.intro .pic{position:absolute;left:647px;top:20px;width:149px;height:150px;background:#fff;box-shadow:0 0 3px #bbb}
.intro .pic div{position:absolute;left:6px;top:6px;width:137px;height:138px;background:linear-gradient(#b49a5e,#6d5a45 45%,#1d1d22)}
.cta{font-family:Ubuntu,sans-serif;font-size:19px;color:#fff;text-align:center;border-radius:8px;line-height:47px}
.cta.gold{background:linear-gradient(var(--gold),var(--gold-dark))}
.cta.blue{background:linear-gradient(var(--blue),var(--blue-dark))}
.card{background:linear-gradient(#fff,#ececec);border:1px solid var(--line);border-radius:7px}
.card-title{position:absolute;left:5px;top:5px;right:5px;height:31px;border-radius:7px;font-family:Ubuntu,sans-serif;font-size:17px;color:#fff;line-height:31px;padding-left:18px}
.card-title.gold{background:linear-gradient(var(--gold),var(--gold-dark))}
.card-title.blue{background:linear-gradient(var(--blue),var(--blue-dark))}
.card p{position:absolute;font-size:9.5px;line-height:13.5px;color:var(--ink)}
.more{position:absolute;bottom:-6px;width:80px;height:19px;border-radius:10px;background:#e3e3e3;border-bottom:3px solid #333;font-size:9px;font-weight:700;text-align:center;line-height:17px}
.news{left:311px;top:799px;width:380px;height:263px;background:#fff;border:1px solid var(--line);border-radius:7px}
.item{position:absolute;left:10px;width:360px;height:80px}
.item + .item{border-top:1px dotted #999}
.thumb{position:absolute;left:3px;top:14px;width:84px;height:56px;border:3px solid #ddd}
.item h3{position:absolute;left:102px;top:15px;font-family:Arimo,sans-serif;font-size:10.5px;color:var(--gold-dark);font-weight:700}
.item p{position:absolute;left:102px;top:30px;width:255px;font-family:Arimo,sans-serif;font-size:8.5px;line-height:13px;color:#333}
.item a{position:absolute;left:103px;top:58px;font-family:Arimo,sans-serif;font-size:9.5px;font-style:italic;color:var(--blue-dark)}
.item .btns{position:absolute;left:285px;top:58px;display:flex;gap:5px;font-family:Arimo,sans-serif;font-size:6.5px}
.btns span{padding:1px 4px;border-radius:2px}
.btns .s{background:#3b5a98;color:#fff}
.btns .t{background:#eef6fb;border:1px solid #cde;color:#1c7fb0}
.footer{left:0;top:1093px;width:1001px;height:107px;background:var(--footer);border-top:8px solid #444}
.footer p{position:absolute;left:92px;font-family:Arimo,sans-serif;font-size:10.5px;color:#bbb}
.partner{position:absolute;font-family:Arimo,sans-serif;color:#aaa;font-size:10px;line-height:12px;letter-spacing:.5px}
</style>
</head>
<body>
<div class="page">

  <div class="abs topbar">
    <a class="media" style="left:233px">ClipCast</a>
    <a class="share">SHARE</a>
    <a style="left:377px">Contact</a>
    <a style="left:441px">Related Sites</a>
    <a style="left:536px">Donate</a>
    <a style="left:601px">Sitemap</a>
    <a style="left:668px">Français</a>
    <a style="left:736px">Member Login</a>
    <a class="pill">Not a member</a>
  </div>

  <header class="abs header">
    <div class="abs brand" style="top:29px"><i></i>PNHH</div>
    <div class="abs fontsize" style="top:21px">Font Size
      <span class="c" style="width:24px;height:24px;font-size:8px">A</span>
      <span class="c" style="width:27px;height:27px;font-size:13px">A</span>
      <span class="c" style="width:29px;height:29px;font-size:17px">A</span>
    </div>
    <div class="abs connect" style="top:22px">Connect us&nbsp;<b></b><b></b><b class="sq"></b><b class="sq"></b></div>
    <div class="abs search" style="top:62px">
      <svg width="20" height="20" style="position:absolute;left:8px;top:6px"><circle cx="8" cy="8" r="5" fill="none" stroke="#333" stroke-width="2"/><line x1="12" y1="12" x2="17" y2="17" stroke="#333" stroke-width="2.5"/></svg>
    </div>
  </header>

  <section class="abs hero">
    <div class="frame"><div class="photo" role="img" aria-label="Heritage hall building at dusk across a snowy field"></div></div>
  </section>

  <nav class="abs nav">
    <span class="home">Home</span>
    <i style="left:156px"></i><span style="left:175px">About</span>
    <i style="left:229px"></i><span style="left:251px">Support PNHH</span>
    <i style="left:349px"></i><span style="left:370px">Events</span>
    <i style="left:424px"></i><span style="left:446px">Projects &amp; Programs</span>
    <i style="left:572px"></i><span style="left:595px">Meet the Patrons</span>
    <i style="left:711px"></i><span style="left:734px">Volunteers</span>
    <i style="left:803px"></i><span style="left:826px">Publications</span>
  </nav>

  <div class="abs tab active" style="left:94px;width:138px">Be a Patron</div>
  <div class="abs tab" style="left:238px;width:147px">Be a Donor</div>
  <div class="abs tab" style="left:390px;width:142px;top:543px;height:35px">Be a Volunteer</div>

  <section class="abs intro">
    <p style="top:27px">You are invited to become a patron. Help us help the Northern Heritage Hall to support the Hall in its mission to educate, preserve and commemorate the nation’s heritage.</p>
    <p style="top:75px">The patrons fulfill our mandate by raising funds for acquisitions and programs, providing volunteers in the galleries and conducting special events at the Hall.</p>
    <div class="pic"><div role="img" aria-label="Three volunteers standing together in a gallery"></div></div>
  </section>

  <div class="abs cta gold" style="left:86px;top:800px;width:200px">Become a Volunteer</div>
  <div class="abs cta blue" style="left:87px;top:867px;width:200px">Donate Now</div>

  <div class="abs card" style="left:87px;top:930px;width:202px;height:128px">
    <div class="card-title gold">Speaker's Bureau</div>
    <p style="left:11px;top:50px;width:182px">Lorem Ipsum is simply dummy text of the printing and typesetting industry. Lorem Ipsum has been the industry's standard dummy text....</p>
    <div class="more" style="left:118px">read more »</div>
  </div>

  <section class="abs news">
    <div class="item" style="top:0">
      <div class="thumb" style="background:linear-gradient(#1c2b3f,#5a6f86)" role="img" aria-label="Jet aircraft on display in a gallery"></div>
      <h3>Business Communication Headline News:</h3>
      <p>Find out what's going on in the world of corporate and business communications.</p>
      <a>Contineue Reading</a>
      <div class="btns"><span class="s">SHARE</span><span class="t">Post</span></div>
    </div>
    <div class="item" style="top:84px">
      <div class="thumb" style="background:linear-gradient(#25332e,#76807a)" role="img" aria-label="Armoured vehicle in an exhibit hall"></div>
      <h3>Business Communication Headline News:</h3>
      <p>Find out what's going on in the world of corporate and business communications.</p>
      <a>Contineue Reading</a>
      <div class="btns"><span class="s">SHARE</span><span class="t">Post</span></div>
    </div>
    <div class="item" style="top:170px">
      <div class="thumb" style="background:linear-gradient(#4c8fc4,#d9ecf7)" role="img" aria-label="Two jets flying in a blue sky"></div>
      <h3>Business Communication Headline News:</h3>
      <p>Find out what's going on in the world of corporate and business communications.</p>
      <a>Contineue Reading</a>
      <div class="btns"><span class="s">SHARE</span><span class="t">Post</span></div>
    </div>
  </section>

  <div class="abs card" style="left:707px;top:799px;width:202px;height:114px">
    <div class="card-title blue">Photo Gallery</div>
    <div class="abs" style="left:11px;top:40px;width:182px;height:67px;background:linear-gradient(#8fb0d2,#2d4a73 45%,#14243d)" role="img" aria-label="Submarine surfacing at sea"></div>
  </div>

  <div class="abs card" style="left:707px;top:928px;width:202px;height:133px">
    <div class="card-title gold">Member Treasures</div>
    <div class="abs" style="left:14px;top:41px;width:100px;height:45px;background:linear-gradient(90deg,#5a3324,#b68c4c,#4c3d3a)" role="img" aria-label="Row of service medals"></div>
    <p style="left:121px;top:43px;width:78px">Ipsum is simply dummy text of the prin.....</p>
    <p style="left:12px;top:92px;width:185px">Lorem Ipsum is simply dummy text of the printing and,.....</p>
    <div class="more" style="left:120px">read more »</div>
  </div>

  <footer class="abs footer">
    <p style="top:40px">Copyright 2013 Patrons of the Northern Heritage Hall. All Rights Reserved.</p>
    <p style="top:60px">12 Harbour Lane, Fairview, Ontario K0X 2B4</p>
    <div class="partner" style="left:620px;top:40px;font-weight:700">Passing<br>the Flame</div>
    <div class="partner" style="left:700px;top:40px;text-align:left">NORTHERN<br>HERITAGE HALL</div>
    <div class="abs" style="left:790px;top:40px;width:24px;height:24px;background:#777"></div>
  </footer>

</div>
</body>
</html>
```